varo institute
Professional
Kemalettin Yurdak
Principal
Elementary School
48 Maple Rd.Scarborough,ON. M1K3P9
Tel:416-5521963 Fax:416-5521964
High School
217 Bellwood Road.Toronto, ON. M9M4R2
Tel:416-3760294 Fax:416-3760287
k.yurdak@varoinstitute.com
www.varoinstitute.com

```html
<!DOCTYPE html>
<html lang="en">
<head>
<meta charset="utf-8">
<title>varo institute — Stationery Concepts</title>
<link href="https://fonts.googleapis.com/css2?family=Open+Sans:wght@400;600;800&display=swap" rel="stylesheet">
<style>
  :root{
    --stage:#1c1c1d;
    --paper:#ffffff;
    --envelope-inner:#eef0f2;
    --blue:#1f8fd2;
    --blue-deep:#1669a8;
    --orange:#f26a2c;
    --ink:#4a4f57;
    --faint:#f6d9cf;
    --caption:#8a8f96;
  }
  *{box-sizing:border-box;margin:0;padding:0}
  html,body{width:1200px;height:586px;overflow:hidden}
  body{background:var(--stage);font-family:"Open Sans",Arial,sans-serif;position:relative;color:var(--ink)}

  .brand{display:flex;align-items:center;gap:5px;color:var(--blue);font-weight:800;line-height:.95}
  .brand-dot{border-radius:50%;background:var(--orange);flex:none}
  .brand-name{text-transform:uppercase;letter-spacing:.02em;white-space:nowrap}

  .hero-brand{position:absolute;left:36px;top:30px}
  .hero-brand .brand-dot{width:30px;height:30px}
  .hero-brand .brand-name{font-size:26px}
  .concept-title{position:absolute;left:78px;top:124px;font-size:12px;color:var(--blue)}

  .caption{position:absolute;font-size:7px;color:var(--caption);white-space:nowrap}

  .card{position:absolute;left:58px;width:163px;height:139px;background:var(--paper);overflow:hidden}
  .card-front{top:211px}
  .card-back{top:384px}
  .card .brand{position:absolute;left:9px;top:10px}
  .card .brand-dot{width:9px;height:9px}
  .card .brand-name{font-size:9px}
  .card-holder{position:absolute;right:9px;top:36px}
  .holder-name{font-size:5.5px;font-weight:800;color:var(--blue-deep)}
  .holder-role{font-size:4.2px}
  .card-contact{position:absolute;left:9px;top:58px;font-size:3.6px;line-height:1.4;white-space:nowrap}
  .card-contact b{color:var(--blue-deep);font-weight:600}
  .card-wave{position:absolute;left:0;bottom:0;width:100%}
  .card-front .card-wave{height:34px}
  .card-back .card-wave{height:50px}
  .card-back .card-contact{color:var(--paper);top:98px}
  .card-back .card-contact b{color:var(--paper)}

  .letterhead{position:absolute;left:298px;top:34px;width:379px;height:489px;background:var(--paper);overflow:hidden}
  .letterhead .brand{position:absolute;left:20px;top:16px}
  .letterhead .brand-dot{width:13px;height:13px}
  .letterhead .brand-name{font-size:12px}
  .letter-contact{position:absolute;left:272px;top:12px;list-style:none;font-size:4.2px;line-height:1.9;white-space:nowrap}
  .letter-contact li::before{content:"";display:inline-block;width:4px;height:4px;border-radius:1px;background:var(--blue);margin-right:3px;vertical-align:middle}
  .letter-mark{position:absolute;left:130px;top:190px;width:116px;height:116px;border-radius:50%;border:10px solid var(--faint)}
  .letter-wave{position:absolute;left:0;bottom:0;width:100%;height:40px}

  .envelopes{position:absolute;left:696px;top:34px;width:456px;height:489px}
  .envelope-stack{position:absolute;left:0;top:0}
  .envelope-front{position:absolute;left:0;top:290px;width:456px;height:199px;background:var(--paper);overflow:hidden}
  .envelope-front .brand{position:absolute;left:14px;top:14px}
  .envelope-front .brand-dot{width:13px;height:13px}
  .envelope-front .brand-name{font-size:12px}
  .envelope-address{position:absolute;left:14px;top:50px;font-size:4.2px;line-height:1.5;white-space:nowrap}
  .envelope-mark{position:absolute;right:60px;top:70px;width:80px;height:80px;border-radius:50%;border:7px solid var(--faint)}
</style>
</head>
<body>

<header class="hero-brand brand"><span class="brand-dot"></span><span class="brand-name">varo<br>institute</span></header>
<p class="concept-title">Stationary Concepts</p>

<article class="card card-front">
  <div class="brand"><span class="brand-dot"></span><span class="brand-name">varo<br>institute</span></div>
  <div class="card-holder"><p class="holder-name">Kemalettin Yurdak</p><p class="holder-role">Principal</p></div>
  <div class="card-contact">
    <p><b>Elementary School</b> 48 Maple Rd.Scarborough,ON. M1K3P9</p>
    <p>Tel:416-5521963 Fax:416-5521964</p>
    <p><b>High School</b> 217 Bellwood Road.Toronto, ON. M9M4R2</p>
    <p>Tel:416-3760294 Fax:416-3760287</p>
    <p>k.yurdak@varoinstitute.com · www.varoinstitute.com</p>
  </div>
  <svg class="card-wave" viewBox="0 0 163 34" preserveAspectRatio="none">
    <path d="M0 20 C55 8 110 30 163 14 V34 H0Z" fill="var(--blue)"/>
    <path d="M0 15 C55 3 110 25 163 9" stroke="var(--orange)" stroke-width="2.5" fill="none"/>
  </svg>
</article>
<p class="caption" style="left:110px;top:355px">Business Card Option 1</p>

<article class="card card-back">
  <div class="brand"><span class="brand-dot"></span><span class="brand-name">varo<br>institute</span></div>
  <div class="card-holder"><p class="holder-name">Kemalettin Yurdak</p><p class="holder-role">Principal</p></div>
  <svg class="card-wave" viewBox="0 0 163 50" preserveAspectRatio="none">
    <path d="M0 12 C55 26 110 0 163 10 V50 H0Z" fill="var(--blue)"/>
    <path d="M0 7 C55 21 110 -5 163 5" stroke="var(--orange)" stroke-width="2.5" fill="none"/>
  </svg>
  <div class="card-contact">
    <p><b>Elementary School</b> 48 Maple Rd.Scarborough,ON. M1K3P9</p>
    <p>Tel:416-5521963 Fax:416-5521964</p>
    <p><b>High School</b> 217 Bellwood Road.Toronto, ON. M9M4R2</p>
    <p>Tel:416-3760294 Fax:416-3760287</p>
  </div>
</article>
<p class="caption" style="left:110px;top:530px">Business Card Option 2</p>

<article class="letterhead">
  <div class="brand"><span class="brand-dot"></span><span class="brand-name">varo<br>institute</span></div>
  <ul class="letter-contact">
    <li>48 Maple Rd.Scarborough,ON. M1K3P9</li>
    <li>Tel:416-5521963</li>
    <li>217 Bellwood Road.Toronto, ON. M9M4R2</li>
    <li>Tel:416-3760294</li>
    <li>www.varoinstitute.com</li>
  </ul>
  <div class="letter-mark"></div>
  <svg class="letter-wave" viewBox="0 0 379 40" preserveAspectRatio="none">
    <path d="M0 22 C125 6 250 36 379 12 V40 H0Z" fill="var(--blue)"/>
    <path d="M0 16 C125 0 250 30 379 6" stroke="var(--orange)" stroke-width="4" fill="none"/>
  </svg>
</article>
<p class="caption" style="left:466px;top:536px">Letterhead</p>

<section class="envelopes">
  <svg class="envelope-stack" width="456" height="300" viewBox="0 0 456 300">
    <rect x="40" y="0" width="416" height="190" fill="var(--paper)"/>
    <path d="M40 0 H456 L248 110 Z" fill="var(--orange)"/>
    <circle cx="248" cy="62" r="18" fill="var(--paper)"/>
    <rect x="20" y="70" width="436" height="220" fill="var(--envelope-inner)"/>
    <path d="M20 70 H456 L238 180 Z" fill="var(--blue)"/>
    <circle cx="238" cy="130" r="18" fill="var(--paper)"/>
  </svg>
  <div class="envelope-front">
    <div class="brand"><span class="brand-dot"></span><span class="brand-name">varo<br>institute</span></div>
    <div class="envelope-address">
      <p>48 Maple Rd.Scarborough,ON. M1K3P9</p>
      <p>217 Bellwood Road.Toronto, ON. M9M4R2</p>
    </div>
    <div class="envelope-mark"></div>
  </div>
</section>
<p class="caption" style="left:1110px;top:536px">Envelopes</p>

</body>
</html>
```